Flyer-Design für europäisches Forschungsprojekt
Beschreibung
Bei diesem Projekt handelt es sich um ein europäisches Forschungsprojekt aus dem Bereich Telekommunikation.
Ziel
The MELOTRA project plans to bring together a novel high frequency advanced radio architecture and an Artificial Intelligence (AI) network processing and management approach into a new type of intelligent communications system Beyond 5G. The new intelligent system approach is necessary because the scale and complexity of the new radio attributes in the new frequency ranges cannot be optimally operated using traditional network management approaches.
Allgemeine Informationen zum Thema:
Projekt Website: http://vbn-melotra.eu
Aufgabenstellung
Wir möchten einen professionellen Flyer, der über das Projekt und seine Zielsetzungen informiert. Zielgruppe sind Fachleute aus diesem Forschungsbereich und Projektteilnehmer.
Sprachliche Anforderung
Projektsprache ist Englisch.
In den Dateien befindet sich eine Word-Datei, die einen Überblick über die Inhalte liefern soll.
Lediglich die enthaltenen Text-Informationen sind 1:1 zu übernehmen, ebenso müssen die Grafiken verwendet werden. Wichtig ist eine vollständige Aufnahme der am Projekt beteiligten Partner in Form ihrer Logos. Ebenso muss eine EU Flagge enthalten sein, sowie das Melotra-Projektlogo.
Die gesamte Gestaltung und Anordnung der Informationen ist selbstverständlich Ihnen überlassen.
Der Flyer sollte übliche DIN Maße haben. Bitte rechnen sie mind. 1 mm Beschnitt auf jeder Außenseite ein. Die Anzahl der Seiten (und Falzen) ist Ihnen überlassen.
Wichtig ist, dass wir nachbearbeitbare Roh-Dateien erhalten. (Z.B: .ai, .eps, .indd )
Wir freuen uns auf Ihre kreativen Vorschläge.

```html
<!DOCTYPE html>
<html lang="en">
<head>
<meta charset="utf-8">
<title>MELOTRA – Objectives and Vision</title>
<link href="https://fonts.googleapis.com/css2?family=Arimo:ital,wght@0,400;0,700;1,400&family=Roboto+Condensed:wght@700&family=Open+Sans:ital,wght@0,600;0,700;1,600&display=swap" rel="stylesheet">
<style>
  :root {
    --brand-blue: #1e6ea6;
    --logo-blue: #5aa6cf;
    --ink: #2b2b2b;
    --heading: #3a3a3a;
    --bg-top: #ffffff;
    --bg-bottom: #b7babd;
    --objectives: #f59a8e;
    --actions: #8fd24f;
    --demos: #b9a2d8;
    --kpi: #cfe9f6;
    --row-band: rgba(230,230,230,0.72);
    --dash-red: #d9534f;
    --label-blue: #4f8fc4;
    --icon-blue: #3f8fc0;
  }
  * { box-sizing: border-box; margin: 0; padding: 0; }
  html, body { width: 1200px; height: 2541px; overflow: hidden; }
  body { font-family: "Arimo", Arial, sans-serif; color: var(--ink); background: #fff; }
  .flyer { position: relative; width: 1200px; height: 2541px; }
  .upper {
    position: absolute; left: 0; top: 0; width: 1200px; height: 2160px;
    background: linear-gradient(180deg, var(--bg-top) 0%, #eeeeef 40%, #d7d9db 75%, var(--bg-bottom) 100%);
  }
  .brand { position: absolute; left: 102px; top: 82px; display: flex; align-items: center; gap: 16px; }
  .brand-dot { width: 66px; height: 66px; border-radius: 50%; background: var(--logo-blue); }
  .brand-name { font-family: "Arimo", sans-serif; font-weight: 400; font-size: 84px; letter-spacing: 6px; color: var(--logo-blue); line-height: 1; }
  .page-title {
    position: absolute; left: 676px; top: 116px; font-family: "Roboto Condensed", sans-serif;
    font-weight: 700; font-size: 48px; color: var(--brand-blue); letter-spacing: 0.2px;
  }
  h2 { position: absolute; left: 101px; font-size: 29px; font-weight: 700; color: var(--heading); }
  .intro-h { top: 228px; }
  .intro { position: absolute; left: 101px; top: 272px; width: 1020px; font-size: 24px; line-height: 34.2px; list-style: none; }
  .intro li { padding-left: 15px; text-indent: -15px; }
  .intro li::before { content: "- "; }

  /* Table */
  .matrix { position: absolute; left: 107px; top: 634px; width: 983px; height: 520px; }
  .col-head { position: absolute; top: 6px; font-size: 17px; font-weight: 700; font-family: "Open Sans", sans-serif; text-align: center; }
  .col { position: absolute; top: 36px; height: 482px; border-radius: 26px; }
  .col.objectives { left: 150px; width: 238px; background: var(--objectives); }
  .col.actions { left: 392px; width: 253px; background: var(--actions); }
  .col.demos { left: 651px; width: 218px; background: var(--demos); }
  .col.kpi { left: 873px; width: 106px; top: 36px; height: 484px; border-radius: 0; background: linear-gradient(180deg, #e6f4fb, var(--kpi)); border: 1px solid #a9d2e8; }
  .row-band { position: absolute; left: 0; width: 872px; height: 108px; border-radius: 18px; background: var(--row-band); }
  .cell { position: absolute; font-family: "Open Sans", sans-serif; font-weight: 600; font-size: 13.5px; line-height: 18.5px; color: #222; }
  .cell.center { text-align: center; }
  .cell ul { list-style: none; }
  .cell li::before { content: "• "; }
  .kpi-text {
    position: absolute; left: 892px; top: 470px; transform: rotate(-90deg); transform-origin: 0 0;
    font-family: "Open Sans", sans-serif; font-weight: 600; font-size: 13.5px; line-height: 19px; white-space: nowrap;
  }

  .pillars-h { top: 1184px; }
  .pillars { position: absolute; left: 101px; top: 1220px; width: 1030px; font-size: 24px; line-height: 34.2px; list-style: none; }
  .pillars li { padding-left: 28px; text-indent: -28px; }
  .concept-h { top: 1504px; }

  /* Concept diagram */
  .concept { position: absolute; left: 103px; top: 1563px; width: 990px; height: 520px; background: #fff; border-radius: 16px; }
  .area-label { position: absolute; top: 8px; width: 220px; text-align: center; font-family: "Open Sans", sans-serif; font-style: italic; font-weight: 600; font-size: 15px; line-height: 19px; color: var(--label-blue); }
  .dash-box { position: absolute; border: 2px dashed var(--dash-red); border-radius: 22px; }
  .tiny { position: absolute; font-family: "Open Sans", sans-serif; font-weight: 600; font-size: 12.5px; line-height: 16px; color: #333; text-align: center; }
  .kpi-red { font-family: "Open Sans", sans-serif; font-weight: 700; font-size: 17px; color: #d22; position: absolute; }
  .art { position: absolute; border-radius: 6px; }
  .art.gray { background: linear-gradient(135deg, #f0f0f0, #c9ccd0); }
  .art.blue { background: linear-gradient(135deg, #2a5fae, #7fb6ea); }
  .art.deep { background: linear-gradient(90deg, #0a2a55, #1f6fc0, #0a2a55); }
  .art.green { background: linear-gradient(135deg, #2d8f3a, #7cc36c); }
  .art.tan { background: linear-gradient(135deg, #efd9b4, #c9a66f); }
  .art.plot { background: linear-gradient(180deg, #ffffff, #e8eef5); border: 1px solid #c5ccd4; }
  .art.multi { background: linear-gradient(135deg, #e9b7a7, #b9cde6, #e7d49a); }
  .art.purple { background: linear-gradient(135deg, #3b2c86, #8e8be8); }

  /* Contact */
  .contact-h { top: 2198px; }
  .contact { position: absolute; left: 101px; top: 2248px; list-style: none; }
  .contact li { display: flex; align-items: center; height: 55px; font-size: 37px; font-weight: 700; color: #2b2b2b; }
  .contact svg { width: 44px; height: 44px; margin-right: 22px; flex: none; }
</style>
</head>
<body>
<div class="flyer">
  <div class="upper"></div>

  <header>
    <div class="brand"><span class="brand-dot"></span><span class="brand-name">MELOTRA</span></div>
    <div class="page-title">Objectives and Vision</div>
  </header>

  <h2 class="intro-h">MELOTRA</h2>
  <ul class="intro">
    <li>Aspires bringing 5G wireless thinking to a long term vision of pervasive mobile virtual services, with computing and connectivity functions managed in an integrated way</li>
    <li>Envisions a unified system beyond 5G, bringing together anovel high frequency advanced radio architecture with an Artificial Intelligence network processing and management approach</li>
    <li>Aims to implement and showcase a PoC of a beyond 5G wireless communications networks concept addressing machine learning based dynamic ultra-high spectral efficient and reliable communications in the bandwidth-rich D-band and intelligent network management in both “Line of Sight” (LOS) and “Non-Line of Sight” (NLOS) environments</li>
  </ul>

  <section class="matrix">
    <div class="col-head" style="left:0;width:150px;">Pillars</div>
    <div class="col-head" style="left:150px;width:238px;">Objectives</div>
    <div class="col-head" style="left:392px;width:253px;">Actions</div>
    <div class="col-head" style="left:651px;width:218px;">Demos</div>
    <div class="col-head" style="left:873px;width:110px;">Main KPIs</div>

    <div class="col objectives"></div>
    <div class="col actions"></div>
    <div class="col demos"></div>
    <div class="col kpi"></div>

    <div class="row-band" style="top:93px;"></div>
    <div class="row-band" style="top:232px;"></div>
    <div class="row-band" style="top:375px;"></div>

    <div class="cell center" style="left:6px;top:105px;width:140px;font-size:15px;line-height:22px;">D-band for 100 Gbit/s reliable wireless connectivity</div>
    <div class="cell center" style="left:170px;top:110px;width:200px;">100 Gbit/s capable, energy and spectral-efficient D-Band wireless B5G networks</div>
    <div class="cell" style="left:420px;top:102px;width:220px;"><ul><li>D-band front-end</li><li>Baseband DSP</li><li>Adaptive spatial SP</li><li>High gain D-band antennas</li><li>Channel modelling</li></ul></div>
    <div class="cell center" style="left:660px;top:128px;width:200px;">P2P D-band LOS outdoor demo</div>

    <div class="cell center" style="left:6px;top:244px;width:140px;font-size:15px;line-height:22px;">Communications beyond the Shannon paradigm</div>
    <div class="cell center" style="left:165px;top:252px;width:210px;">Ultra-reliable D-band connectivity and reconfigurability in all usage environments</div>
    <div class="cell" style="left:420px;top:244px;width:220px;"><ul><li>Reconfigurable adaptive metasurface design</li><li>Beamforming for LOS and NLOS links</li><li>MAC design</li></ul></div>
    <div class="cell center" style="left:660px;top:270px;width:200px;">Metasurface-based D-band demo</div>

    <div class="cell center" style="left:6px;top:388px;width:140px;font-size:15px;line-height:22px;">Artificial Intelligence-based wireless system concept</div>
    <div class="cell center" style="left:165px;top:394px;width:210px;">Transform networks B5G into intelligent connectivity/computing platforms</div>
    <div class="cell" style="left:418px;top:385px;width:225px;"><ul><li>ML for channel modelling</li><li>ML-based resource allocation and energy efficiency ML for network deployment optimization</li></ul></div>
    <div class="cell center" style="left:660px;top:412px;width:200px;">Intelligent D-band Network Demo</div>

    <div class="kpi-text">100 Gbps throughput<br>100m range<br>Massive number of devices<br>Zero latency<br>Ultra-high reliability</div>
  </section>

  <h2 class="pillars-h">The MELOTRA Pillars</h2>
  <ol class="pillars">
    <li>1. Develop new radio technologies for communications using the above 100Ghz D-Band frequency ranges.</li>
    <li>2. Exploit emerging advanced connectivity approaches based on metasurfaces and shaping propagation environments in D-band</li>
    <li>3. Employ Artificial Intelligence to high-frequency communications resource management with dynamic assignment and reconfiguration of metasurfaces to provide continuous and reliable high-bandwidth connections in a Beyond-5G scenario</li>
  </ol>

  <h2 class="concept-h">MELOTRA system concept for networks beyond 5G</h2>
  <section class="concept">
    <div class="area-label" style="left:7px;">Key performance<br>Indicators</div>
    <div class="area-label" style="left:240px;">Fundamental<br>characteristics</div>
    <div class="area-label" style="left:482px;">Enabling<br>technologies</div>
    <div class="area-label" style="left:735px;">Key technology<br>modules</div>

    <div class="dash-box" style="left:5px;top:52px;width:238px;height:312px;"></div>
    <div class="kpi-red" style="left:18px;top:62px;">100 Gbps</div>
    <div class="art gray" style="left:18px;top:90px;width:70px;height:62px;border-radius:50%;" role="img" aria-label="Speed gauge icon"></div>
    <div class="art gray" style="left:108px;top:84px;width:120px;height:30px;" role="img" aria-label="Range link icon"></div>
    <div class="tiny" style="left:108px;top:122px;width:120px;">100m range</div>
    <div class="art blue" style="left:152px;top:150px;width:80px;height:76px;border-radius:50%;" role="img" aria-label="Stopwatch icon for zero latency"></div>
    <div class="tiny" style="left:130px;top:230px;width:110px;">Zero latency</div>
    <div class="art multi" style="left:14px;top:162px;width:104px;height:150px;" role="img" aria-label="Collage of connected devices"></div>
    <div class="tiny" style="left:6px;top:318px;width:120px;">Massive devices</div>
    <div class="art gray" style="left:152px;top:252px;width:64px;height:64px;border-radius:50%;" role="img" aria-label="Target icon for reliability"></div>
    <div class="tiny" style="left:128px;top:318px;width:110px;">Ultra-high reliability</div>

    <div class="dash-box" style="left:250px;top:52px;width:240px;height:312px;"></div>
    <div class="art plot" style="left:272px;top:64px;width:196px;height:140px;" role="img" aria-label="Plot of D-band channel attenuation versus frequency"></div>
    <div class="tiny" style="left:255px;top:214px;width:230px;">D-band LOS/NLOS channel</div>
    <div class="art plot" style="left:268px;top:240px;width:204px;height:54px;" role="img" aria-label="Block diagram of communication theory models"></div>
    <div class="tiny" style="left:255px;top:308px;width:230px;">Communication Theory beyond Shannon</div>

    <div class="dash-box" style="left:497px;top:52px;width:241px;height:312px;"></div>
    <div class="art green" style="left:514px;top:64px;width:100px;height:112px;" role="img" aria-label="Antenna array for beamforming"></div>
    <div class="art gray" style="left:622px;top:64px;width:104px;height:112px;" role="img" aria-label="Beam pattern sketch"></div>
    <div class="tiny" style="left:500px;top:182px;width:235px;">Advanced Beamforming</div>
    <div class="art purple" style="left:554px;top:200px;width:130px;height:86px;" role="img" aria-label="Reconfigurable metasurface illustration"></div>
    <div class="tiny" style="left:500px;top:292px;width:235px;">Reconfigurable metasurfaces design</div>
    <div class="art gray" style="left:540px;top:314px;width:44px;height:44px;border-radius:50%;" role="img" aria-label="Machine learning chip icon"></div>
    <div class="tiny" style="left:596px;top:318px;width:80px;">Machine learning</div>

    <div class="dash-box" style="left:745px;top:52px;width:240px;height:312px;"></div>
    <div class="tiny" style="left:758px;top:100px;width:36px;">DSP</div>
    <div class="art deep" style="left:800px;top:64px;width:172px;height:80px;" role="img" aria-label="Signal waveform with binary data"></div>
    <div class="art green" style="left:764px;top:162px;width:88px;height:80px;" role="img" aria-label="Integrated RFIC board"></div>
    <div class="tiny" style="left:752px;top:246px;width:110px;">Highly integrated RFIC</div>
    <div class="art gray" style="left:880px;top:162px;width:92px;height:66px;" role="img" aria-label="High-gain antenna radiation pattern"></div>
    <div class="tiny" style="left:866px;top:232px;width:120px;">High-gain antennas</div>
    <div class="art tan" style="left:812px;top:282px;width:110px;height:46px;" role="img" aria-label="Metasurface panel"></div>
    <div class="tiny" style="left:790px;top:340px;width:150px;">Metasurfaces</div>

    <div class="dash-box" style="left:5px;top:375px;width:980px;height:142px;"></div>
    <div class="tiny" style="left:30px;top:383px;width:190px;">Backhaul/Fronthaul networks of fixed topology</div>
    <div class="art gray" style="left:70px;top:418px;width:130px;height:90px;" role="img" aria-label="City buildings linked by fixed backhaul"></div>
    <div class="tiny" style="left:380px;top:383px;width:200px;">AdHoc Backhauling</div>
    <div class="art gray" style="left:380px;top:418px;width:200px;height:90px;background:linear-gradient(180deg,#f6f6f6,#dcdfe3);" role="img" aria-label="Drones relaying between towers"></div>
    <div class="tiny" style="left:765px;top:383px;width:190px;">Advanced NLOS connectivity based on metasurfaces</div>
    <div class="art gray" style="left:790px;top:420px;width:140px;height:90px;" role="img" aria-label="Indoor room with metasurface links"></div>
  </section>

  <h2 class="contact-h">Contact Us</h2>
  <ul class="contact">
    <li><svg viewBox="0 0 44 44" fill="none" stroke="var(--icon-blue)" stroke-width="2"><circle cx="22" cy="22" r="20"/><circle cx="22" cy="22" r="10"/><ellipse cx="22" cy="22" rx="4" ry="10"/><line x1="12" y1="22" x2="32" y2="22"/></svg>https://www.vbn-melotra.eu/</li>
    <li><svg viewBox="0 0 44 44" fill="none" stroke="var(--icon-blue)" stroke-width="2"><circle cx="22" cy="22" r="20"/><path d="M13 15h18v11H20l-5 4v-4h-2z" fill="var(--icon-blue)"/></svg>@MelotraVbn&nbsp; https://quipstream.com/MelotraVbn</li>
    <li><svg viewBox="0 0 44 44" fill="none" stroke="var(--icon-blue)" stroke-width="2"><circle cx="22" cy="22" r="20"/><path d="M15 29l2-6 10-10 4 4-10 10z" fill="var(--icon-blue)"/></svg>https://www.vbn-melotra.eu/contact/</li>
    <li><svg viewBox="0 0 44 44" fill="none" stroke="var(--icon-blue)" stroke-width="2"><circle cx="22" cy="22" r="20"/><rect x="12" y="15" width="20" height="14"/><path d="M12 15l10 8 10-8"/></svg>contact@vbn-melotra.eu</li>
  </ul>
</div>
</body>
</html>
```